New business card layout design

We need to revamp our business card layout to be more dynamic and professional. Interested in different card materials. Have a logo and color scheme. Possible something dark background light text, see what works. Will attach current card below, along with our favorite card from your website. Please test interesting ideas out with curves vs straight lines, dark background, dark/light sides, inlaid text, etc.

https://www.verdolinefunds.example/
Here is our website for theme. Let us know if you have ANY questions :)

Target Market(s)

high-net worth accredited investors and fund managers

Industry/Entity Type

Oil and Gas investment fund

Contact Information for Business Card

Name, title, number, email, website, possibly barcode to contact page on website, business name and logo

Colors
0054AA
0677BA
7BADD7
CADEEF
E8F1F8

Requirements
Must have
• Name, title, number, email, website
Nice to have
• barcode to contact page, other ideas?
Should not have
• a pink unicorn

```html
<!DOCTYPE html>
<html lang="en">
<head>
<meta charset="utf-8">
<title>Verdoline Funds – Business Card</title>
<link href="https://fonts.googleapis.com/css2?family=Poppins:wght@400;500;700&display=swap" rel="stylesheet">
<style>
  :root {
    --navy: #1f1e4a;
    --taupe: #aba49c;
    --paper: #ffffff;
    --ink: #1b1b1f;
    --rule: #a59e96;
    --stage: #e4e4e6;
  }
  * { margin: 0; padding: 0; box-sizing: border-box; }
  html, body { width: 1200px; height: 769px; overflow: hidden; }
  body {
    background: var(--stage);
    font-family: "Poppins", Arial, sans-serif;
    color: var(--ink);
    position: relative;
  }
  .card {
    position: absolute;
    width: 540px;
    height: 310px;
    background: var(--paper);
    overflow: hidden;
    box-shadow: 0 10px 30px rgba(0,0,0,.18);
  }
  .card--front { left: 45px; top: 230px; }
  .card--back { left: 615px; top: 230px; }

  .band { position: absolute; background: var(--navy); }
  .band--taupe { background: var(--taupe); }

  /* front side */
  .front-top-band { left: 62px; top: 0; width: 478px; height: 38px; }
  .front-bottom-band { left: 215px; bottom: 0; width: 215px; height: 30px; }
  .badge-square {
    position: absolute; left: 70px; top: 16px;
    width: 38px; height: 38px; border-radius: 9px;
    background: var(--navy); border: 2px solid var(--paper);
    box-shadow: 0 0 0 1px var(--navy);
  }
  .timeline {
    position: absolute; left: 88px; top: 54px;
    width: 2px; height: 150px; background: var(--rule);
  }
  .timeline-icon {
    position: absolute; left: 77px;
    width: 24px; height: 24px; border-radius: 6px;
    background: var(--navy);
    display: flex; align-items: center; justify-content: center;
  }
  .timeline-icon svg { width: 13px; height: 13px; }
  .icon-person { top: 76px; }
  .icon-phone { top: 122px; }
  .icon-mail { top: 152px; }
  .icon-pin { top: 184px; }

  .contact { position: absolute; left: 112px; }
  .person-name { top: 70px; font-size: 21px; line-height: 1.1; font-weight: 400; color: var(--ink); }
  .person-name strong { font-weight: 700; }
  .person-title { top: 96px; font-size: 11px; color: var(--ink); }
  .contact-lines { font-size: 11.5px; line-height: 1.35; }
  .phones { top: 120px; }
  .web { top: 150px; }
  .address { top: 182px; }

  .divider {
    position: absolute; left: 300px; top: 118px;
    width: 1.5px; height: 150px; background: var(--navy);
  }
  .brand {
    position: absolute;
    display: flex; align-items: center; gap: 8px;
    font-weight: 700; color: var(--navy); white-space: nowrap;
    text-transform: uppercase; letter-spacing: .02em;
  }
  .brand-mark { background: var(--navy); flex: none; }
  .brand--front { left: 322px; top: 170px; font-size: 19px; }
  .brand--front .brand-mark { width: 12px; height: 12px; }

  /* back side */
  .back-top-band { left: 160px; top: 30px; width: 345px; height: 32px; }
  .back-bottom-navy-left { left: 0; top: 246px; width: 95px; height: 34px; }
  .back-bottom-taupe { left: 95px; top: 246px; width: 330px; height: 34px; }
  .back-bottom-navy-right { left: 425px; top: 246px; width: 60px; height: 34px; }
  .brand--back { left: 0; right: 0; top: 132px; justify-content: center; font-size: 34px; }
  .brand--back .brand-mark { width: 20px; height: 20px; }
</style>
</head>
<body>

<section class="card card--front" aria-label="Business card, contact side">
  <div class="band front-top-band"></div>
  <div class="band front-bottom-band"></div>
  <div class="badge-square"></div>
  <div class="timeline"></div>

  <div class="timeline-icon icon-person">
    <svg viewBox="0 0 16 16" fill="#fff"><circle cx="8" cy="5" r="3"/><path d="M2 15c0-3.5 2.7-5.5 6-5.5s6 2 6 5.5z"/></svg>
  </div>
  <div class="timeline-icon icon-phone">
    <svg viewBox="0 0 16 16" fill="#fff"><path d="M4 1.5l2.2 3-1.4 1.6c.9 2 2.3 3.4 4.3 4.3l1.6-1.4 3 2.2-1.2 2.6C7.5 13.6 2.4 8.5 1.5 3z"/></svg>
  </div>
  <div class="timeline-icon icon-mail">
    <svg viewBox="0 0 16 16" fill="none" stroke="#fff" stroke-width="1.6"><rect x="2" y="4" width="12" height="9"/><path d="M2 4l6 5 6-5"/></svg>
  </div>
  <div class="timeline-icon icon-pin">
    <svg viewBox="0 0 16 16" fill="#fff"><path d="M8 1a5 5 0 0 0-5 5c0 4 5 9 5 9s5-5 5-9a5 5 0 0 0-5-5zm0 7a2 2 0 1 1 0-4 2 2 0 0 1 0 4z"/></svg>
  </div>

  <p class="contact person-name"><strong>Teodor</strong> Lindqvist</p>
  <p class="contact person-title">CEO &amp; Founder</p>
  <p class="contact contact-lines phones">000 111 222 333<br>000 111 222 333</p>
  <p class="contact contact-lines web">yourgmail@name.com<br>www.websitename.com</p>
  <p class="contact contact-lines address">Your Street Adrees Here<br>New Yerk, sity - 000</p>

  <div class="divider"></div>

  <div class="brand brand--front"><span class="brand-mark"></span>Verdoline Funds</div>
</section>

<section class="card card--back" aria-label="Business card, brand side">
  <div class="band back-top-band"></div>
  <div class="band back-bottom-navy-left"></div>
  <div class="band band--taupe back-bottom-taupe"></div>
  <div class="band back-bottom-navy-right"></div>
  <div class="brand brand--back"><span class="brand-mark"></span>Verdoline Funds</div>
</section>

</body>
</html>
```